Bright Paths Together Charity Golf Tournament

we are looking for help designing a trifold brochure that could accompany the attached letter, both being mailed in a #10 envelope. With the amount of sponsorship copy, it be a good idea to put the detailed sponsorship level content on a single one-page flyer. One section of the trifold could be a summary level of the sponsorship level and allow the sponsor tear-off that part and mail in their payment. I want the color scheme and design to align with our website https://brightpathstogether.org while not losing sight that this is a charity golf tournament. The sponsorship detail is not finalized but is directionally correct as shown on page 2 of the letter. What might be ideal is to have a tri-fold, a bi-fold which would contain details of the event along with the copy on the letter, while the one-page flyer would have the detailed sponsor levels & details.

I would also be open to alternative ideas if you think there's a better way of doing this. For example, could we put everything into a one 2-page brochure that would be the same size as the letter. There could be a tear out to mail back but this could fit into an envelope that could accommodate an unfolded 8.5x11 letter. I think this could work but will let you think about best options.

Target Market(s)

Corporate sponsors and serious golfers

Industry/Entity Type

Non-Profit

Font styles to use
Serif

Requirements
Must have
• Event Date: August 23, 2021
Event Location: Maple Ridge County Club, 47 Orchard Lane, Glenside PA
Schedule:
Lunch: 11:00
Shotgun Start: 12:30
Open Bar Reception: 5:00
Dinner: 6:00

At the moment, the sponsorship levels, pricing, and inclusions are directionally correct.

BPT Brand Colors:
#08143A
#FFCD35
#980909
#11808B
#3C2C83

Ok to use any images from the Maple Ridge CC website.
Nice to have
• We have a lot of copy & content to share, so I am not locked into a trifold - bifold concept if a single full size 2-sheet (8 pages) would work better as long as there would be a way for the sponsor to 'tear off' the summary order form. If you think the full size version is a better single option to go with our letter, I would like to use some images from our website along to give the event the seriousness it deserves while still being a golf tournament. This will be our first annual tournament although I am not sure that's important to include.
Should not have
• emojis, clip art.

```html
<!DOCTYPE html>
<html lang="en">
<head>
<meta charset="utf-8">
<title>Bright Paths Together Charity Golf Tournament – Trifold</title>
<link rel="stylesheet" href="https://fonts.googleapis.com/css2?family=Merriweather:wght@400;700;900&family=Montserrat:wght@400;500;600;700;800&display=swap">
<style>
:root{
  --navy:#08143A;
  --gold:#FFCD35;
  --gold-soft:#f6e3a0;
  --lav:#d7dcf0;
  --paper:#ffffff;
  --mist:#ebebeb;
  --ink:#2b2f3a;
  --grass:#4fa62a;
  --bg:#dcdcdc;
}
*{box-sizing:border-box;margin:0;padding:0}
html,body{width:1200px;height:2180px;overflow:hidden;background:var(--bg)}
body{font-family:"Montserrat",sans-serif;color:var(--ink);position:relative}
.spread{position:absolute;left:60px;width:1080px;height:880px;display:flex;box-shadow:0 12px 30px rgba(0,0,0,.18)}
.spread--outside{top:100px}
.spread--inside{top:1100px}
.panel{position:relative;width:360px;height:880px;overflow:hidden}
.serif{font-family:"Merriweather",serif}
.abs{position:absolute}
.photo{position:absolute}

/* ---------- order form panel ---------- */
.form-panel{background:var(--paper)}
.form-panel .swoosh{position:absolute;inset:0}
.form-title{left:34px;top:44px;font-family:"Merriweather",serif;font-weight:700;font-size:15px;line-height:1.3;color:var(--navy)}
.form-note{left:34px;top:90px;width:250px;font-size:9px;line-height:1.35;color:var(--ink)}
.form-check{left:34px;top:124px;font-size:9.5px;font-weight:700;color:var(--navy)}
.levels{position:absolute;left:34px;top:146px;width:262px;border-collapse:collapse;font-size:5.8px;line-height:1.38;color:#333}
.levels td{border:1px solid #b8bdd0;padding:4px 3px 5px;vertical-align:top}
.levels tr:nth-child(odd){background:var(--gold-soft)}
.levels tr:nth-child(even){background:var(--lav)}
.levels .lvl{width:54px}
.levels .lvl::before{content:"";display:inline-block;width:5px;height:5px;border:1px solid #555;background:#fff;margin-right:2px;vertical-align:-1px}
.levels .price{width:28px;text-align:right}
.contact-fields{position:absolute;left:34px;top:606px;width:262px;border-collapse:collapse;font-size:5.6px;font-weight:700;color:var(--navy)}
.contact-fields td{border:1px solid #d0d3dc;height:18px;padding:0 3px}
.contact-fields tr:nth-child(odd) .label{background:var(--lav)}
.contact-fields tr:nth-child(even) .label{background:var(--gold-soft)}
.contact-fields .label{width:54px}
.form-small{font-size:5.6px;color:#444;line-height:1.35}
.sign-line{border-top:1px dashed #888;padding-top:2px}

/* ---------- event panel ---------- */
.event-panel{background:var(--mist)}
.brand-mark{display:flex;align-items:center;gap:6px;font-family:"Merriweather",serif;font-weight:700;color:var(--navy)}
.brand-mark .dot{width:14px;height:14px;border-radius:50%;background:var(--gold);flex:none}
.event-box{left:34px;top:152px;width:292px;height:176px;background:rgba(255,255,255,.93);border:2px solid var(--navy);border-radius:16px;overflow:hidden;z-index:3}
.event-box .facts{display:grid;grid-template-columns:92px 1fr;gap:2px 6px;padding:12px 14px 8px;font-size:8.5px;line-height:1.3}
.event-box .facts dt{font-weight:700;color:var(--navy)}
.event-box .bar{background:var(--gold);color:var(--navy);font-weight:800;font-size:10.5px;padding:4px 14px}
.event-box .sched{display:grid;grid-template-columns:92px 1fr;font-size:8.5px}
.event-box .sched dt,.event-box .sched dd{padding:4px 14px 3px;border-bottom:1px solid #d8d8d8}
.event-box .sched dt{font-weight:700;color:var(--navy);padding-right:0}
.event-box .sched dd{padding-left:6px}
.contacts{left:34px;top:650px;width:300px;display:flex;gap:10px;font-size:8px;line-height:1.45;color:var(--gold)}
.contacts div+div{border-left:1px solid rgba(255,255,255,.5);padding-left:10px}
.contacts strong{font-weight:700;display:block}
.web{font-size:12px;color:#fff;letter-spacing:.2px}
.web b{font-weight:700}

/* ---------- cover panel ---------- */
.cover-panel{background:var(--navy)}
.cover-title{left:0;width:360px;top:664px;text-align:center}
.cover-title .kicker{font-family:"Merriweather",serif;font-weight:700;font-size:15px;color:#fff}
.cover-title .kicker span{color:var(--gold)}
.cover-title .golf{font-family:"Montserrat",sans-serif;font-weight:800;font-size:62px;line-height:1;color:var(--gold);letter-spacing:2px;margin-top:6px}
.cover-title .tour{font-family:"Montserrat",sans-serif;font-weight:800;font-size:22px;color:#fff;letter-spacing:1px;margin-top:2px}

/* ---------- letter panel ---------- */
.letter-panel{background:var(--paper)}
.proposal-title{left:34px;top:228px;font-family:"Merriweather",serif;font-weight:900;font-size:30px;line-height:1.24;color:var(--navy)}
.salute{left:34px;top:422px;font-size:13px;font-weight:700;color:var(--navy)}
.letter-copy{left:34px;top:450px;width:274px;font-size:7.3px;line-height:1.45;color:#333}
.letter-copy p+p{margin-top:8px}
.grass{left:0;bottom:0;width:100%;height:34px;background:linear-gradient(180deg,#a6dc63,#6cbc36 50%,var(--grass))}

/* ---------- partners panel ---------- */
.partners-panel{background:var(--mist)}
.partners-copy{left:40px;top:128px;width:276px;font-size:8.3px;line-height:1.45;color:#333}
.partners-copy h2{font-size:15px;font-weight:700;color:var(--navy);margin-bottom:12px}
.partners-copy h3{font-size:10px;font-weight:700;color:var(--navy);margin-top:16px}
.partners-copy ul{list-style:none;margin-bottom:8px}
.partners-copy li{display:flex;align-items:center;gap:7px;margin-bottom:5px;font-size:8.6px}
.partners-copy p+p{margin-top:14px}
.signoff{font-weight:700;color:var(--navy);font-size:8px}

/* ---------- donate panel ---------- */
.donate-panel{background:var(--navy)}
.donate-copy{left:40px;top:590px;width:290px;color:#fff}
.donate-copy h2{font-family:"Merriweather",serif;font-weight:700;font-size:23px;line-height:1.2}
.donate-copy p{font-size:9.5px;line-height:1.4;margin-top:10px}
.donate-btn{display:inline-block;margin-top:22px;background:var(--gold);color:var(--navy);font-family:"Merriweather",serif;font-weight:700;font-size:12px;padding:10px 12px}
</style>
</head>
<body>

<!-- ============ OUTSIDE SPREAD ============ -->
<section class="spread spread--outside">

  <!-- order form -->
  <article class="panel form-panel">
    <svg class="swoosh" width="360" height="880" viewBox="0 0 360 880" aria-hidden="true">
      <path d="M360 0 L352 0 C342 400 336 700 300 880 L360 880 Z" fill="var(--navy)"/>
      <path d="M340 0 C332 400 324 700 290 880" fill="none" stroke="var(--gold)" stroke-width="4"/>
    </svg>
    <h1 class="abs form-title">2021 Hybrid Golf Event<br>Sponsorship Opportunities</h1>
    <p class="abs form-note">as a 501(c)3 public charity, your sponsorship is tax deductible to the</p>
    <p class="abs form-check">Please Check Box:</p>
    <table class="levels">
      <tr><td class="lvl">Presenting Sponsor</td><td>• Co-naming rights with BPT Beacons of Promise<br>• Banner at course with corporate logo<br>• Corporate info in participant gift bags<br>• Two golf foursomes<br>• Recognition on all marketing materials<br>• Speaking slot at post-tournament dinner</td><td class="price">$7,500</td></tr>
      <tr><td class="lvl">Presenting Co-Sponsor</td><td>• Co-sponsor naming of event with BOP<br>• Banner at course with corporate logo<br>• Putting green sponsorship banner<br>• Corporate info in gift bags<br>• Two golf foursomes<br>• Recognition on marketing materials<br>• Recognition at event dinner</td><td class="price">$5,000</td></tr>
      <tr><td class="lvl">Presenting Co-Sponsor</td><td>• Co-sponsor naming of event with BOP<br>• Putting green sponsorship banner<br>• Corporate info in gift bags<br>• Two golf foursomes<br>• Recognition on marketing materials<br>• Recognition at event dinner</td><td class="price">$5,000</td></tr>
      <tr><td class="lvl">Technology Sponsor</td><td>• Driving range sponsorship banner<br>• One golf foursome<br>• Recognition as technology sponsor<br>• Recognition at event dinner</td><td class="price">$3,000</td></tr>
      <tr><td class="lvl">Corporate Sponsor with Golf Foursome</td><td>One golf foursome<br>Hole sign<br>Recognition on all marketing materials</td><td class="price">$2,500</td></tr>
      <tr><td class="lvl">Pin Flag Sponsor</td><td>• Your logo on a custom pin flag to keep<br>• Recognition on all marketing materials</td><td class="price">$2,500</td></tr>
      <tr><td class="lvl">Golf Cart Sponsor</td><td>• Your logo &amp; brand on all golf carts<br>• Recognition on all marketing materials</td><td class="price">$2,500</td></tr>
      <tr><td class="lvl">Corporate Sponsor without Golf</td><td>• Hole sign<br>• Recognition on all marketing materials<br>• Dinner at event for four</td><td class="price">$2,500</td></tr>
      <tr><td class="lvl">Cigar Roller Sponsor</td><td>Table sign at rolling table and reception<br>• Recognition</td><td class="price">$1,000</td></tr>
      <tr><td class="lvl">Hole Sponsor</td><td>Custom sign at every tee box</td><td class="price">$500</td></tr>
    </table>
    <table class="contact-fields">
      <tr><td class="label">Company Name</td><td></td></tr>
      <tr><td class="label">Contact Person</td><td></td></tr>
      <tr><td class="label">Contact Phone</td><td></td></tr>
      <tr><td class="label">Contact Email</td><td></td></tr>
      <tr><td class="label">Billing Address</td><td></td></tr>
      <tr><td class="label">City/State/Zip</td><td></td></tr>
    </table>
    <p class="abs form-small" style="left:34px;top:728px;width:262px;text-align:center">Invoices will be sent to the billing address or email address given above.</p>
    <p class="abs form-small sign-line" style="left:34px;top:760px;width:140px">Signature of Sponsor</p>
    <p class="abs form-small sign-line" style="left:196px;top:760px;width:80px">Date</p>
    <p class="abs form-small" style="left:34px;top:790px;width:100px">Please make checks payable to:</p>
    <p class="abs form-small" style="left:136px;top:790px;width:140px">Bright Paths Together BOP Golf Tournament, 58 Linden Street, Doylestown PA 18901</p>
    <p class="abs form-small" style="left:34px;top:822px;width:240px;text-align:center">Please return your completed Sponsorship form June 1, 2021</p>
  </article>

  <!-- event details -->
  <article class="panel event-panel">
    <div class="abs brand-mark" style="left:0;width:360px;top:70px;justify-content:center;font-size:12px"><span class="dot"></span>Beacons of Promise</div>
    <div class="photo" role="img" aria-label="Rolling golf course landscape with trees and a pond at sunset" style="left:0;top:250px;width:360px;height:330px;background:linear-gradient(180deg,#dfe3e2 0%,#c4c9bd 18%,#b8b374 32%,#a7a545 46%,#8ea33a 60%,#6f8c2e 78%,#4e6a22 100%)"></div>
    <div class="photo" role="img" aria-label="Golf ball close-up" style="left:90px;top:440px;width:120px;height:120px;border-radius:50%;background:radial-gradient(circle at 40% 35%,#ffffff,#d9d9d9 70%,#b8b8b8)"></div>
    <svg class="abs" style="left:0;top:540px" width="360" height="340" viewBox="0 0 360 340" aria-hidden="true">
      <path d="M0 40 C90 8 220 0 360 22 L360 340 L0 340 Z" fill="var(--navy)"/>
    </svg>
    <dl class="abs event-box">
      <div class="facts">
        <dt>Event Date:</dt><dd>August 23, 2021</dd>
        <dt>Event Location:</dt><dd>Maple Ridge County Club, 47 Orchard Lane, Glenside PA</dd>
      </div>
      <div class="bar">SCHEDULE:</div>
      <div class="sched">
        <dt>Lunch:</dt><dd>11:00</dd>
        <dt>Shotgun Start:</dt><dd>12:30</dd>
        <dt>Open Bar Reception:</dt><dd>5:00</dd>
        <dt style="border:0">Dinner:</dt><dd style="border:0">6:00</dd>
      </div>
    </dl>
    <div class="abs brand-mark" style="left:0;width:360px;top:606px;justify-content:center;font-size:15px;color:#fff">Bright Paths Together</div>
    <div class="abs contacts">
      <div><strong>Tom Garrity</strong>tom@brightpathstogether.org<br>(267) 555-0148<br>58 Linden Street<br>Doylestown PA 18901</div>
      <div><strong>Ellen Marsh</strong>ellen@brightpathstogether.org<br>(610) 555-0192<br>312 Cedar Avenue<br>Bethlehem, PA 18017</div>
    </div>
    <svg class="abs" style="left:166px;top:770px" width="28" height="28" viewBox="0 0 28 28" aria-hidden="true">
      <circle cx="14" cy="14" r="13" fill="var(--gold)"/>
      <g fill="none" stroke="var(--navy)" stroke-width="1.3"><circle cx="14" cy="14" r="7.5"/><ellipse cx="14" cy="14" rx="3.5" ry="7.5"/><path d="M6.5 14h15M8 10h12M8 18h12"/></g>
    </svg>
    <p class="abs web" style="left:0;width:360px;top:818px;text-align:center">www.<b>brightpathstogether</b>.org</p>
  </article>

  <!-- cover -->
  <article class="panel cover-panel">
    <div class="abs" style="left:0;top:0;width:360px;height:100px;background:var(--paper)"></div>
    <div class="abs serif" style="left:0;width:360px;top:28px;text-align:center;color:var(--navy);font-weight:700">
      <div style="font-size:30px;letter-spacing:2px;line-height:1">BPT</div>
      <div style="font-size:12px;margin-top:6px">Bright Paths Together</div>
    </div>
    <div class="photo" role="img" aria-label="Golfer finishing a swing on a sunlit hillside course" style="left:0;top:100px;width:360px;height:500px;background:linear-gradient(180deg,#eef1f2 0%,#d8dcd6 22%,#c9c48e 38%,#c4a64a 50%,#a49a35 62%,#7f8a2c 78%,#5d6e22 100%)"></div>
    <svg class="abs" style="left:0;top:440px" width="360" height="180" viewBox="0 0 360 180" aria-hidden="true">
      <path d="M0 140 C130 150 270 120 360 20 L360 180 L0 180 Z" fill="var(--navy)"/>
      <path d="M40 148 C170 150 290 110 360 28" fill="none" stroke="var(--gold)" stroke-width="5"/>
    </svg>
    <div class="abs cover-title">
      <div class="kicker">Bright Paths <span>Together Charity</span></div>
      <div class="golf">GOLF</div>
      <div class="tour">TOURNAMENT</div>
      <p class="web" style="margin-top:10px;font-size:14px">www.<b>brightpathstogether</b>.org</p>
    </div>
  </article>
</section>

<!-- ============ INSIDE SPREAD ============ -->
<section class="spread spread--inside">

  <!-- letter -->
  <article class="panel letter-panel">
    <div class="photo" role="img" aria-label="Golf course fairway view with clubhouse in the distance" style="left:0;top:0;width:360px;height:140px;background:linear-gradient(180deg,#6b6a4a 0%,#7f9a48 25%,#a3cf4e 60%,#c4e05a 100%)"></div>
    <svg class="abs" style="left:0;top:40px" width="360" height="200" viewBox="0 0 360 200" aria-hidden="true">
      <path d="M0 190 C90 140 220 80 360 70 L360 200 L0 200 Z" fill="var(--paper)"/>
      <path d="M0 186 C90 136 220 76 360 66" fill="none" stroke="var(--gold)" stroke-width="5"/>
      <circle cx="104" cy="86" r="78" fill="var(--paper)"/>
    </svg>
    <div class="abs brand-mark" style="left:44px;top:108px;font-size:11px;width:120px;flex-direction:column;text-align:center"><span class="dot"></span>Beacons of Promise</div>
    <h1 class="abs proposal-title">2021 HYBRID<br>GOLF EVENT<br>SPONSORSHIP<br>PROPOSAL</h1>
    <h2 class="abs salute">Dear Potential Sponsor:</h2>
    <div class="abs letter-copy">
      <p>The Bright Paths Together BOP (Beacons of Promise) Committee is planning a Charity Hybrid Golf Tournament benefiting adults with autism or other intellectual developmental disabilities in Bucks and Lehigh County. The tournament will be held on Monday, August 23, at the Maple Ridge County Club in Glenside PA.</p>
      <p>Our mission is to offer adults with autism or other intellectual developmental disabilities the opportunity to live as independently as possible by providing safe and secure neuro-inclusive cohousing communities with built-in amenities and natural support systems and to give their parents and aging caregivers peace of mind that they will never have to worry about their children being alone or isolated.</p>
      <p>We are actively confronting the unique and unmet housing needs and challenges higher-functioning autistic adults and other at-risk individuals face when their parents can no longer care for them. The alternative can be heartbreaking. Instead, we provide neuro-inclusive 'smart-home enabled' cohousing communities for this underserved population, allowing them to not only live as independently as possible, but seek meaningful employment and be an integral and active part of their local community.</p>
      <p>We are pleased to announce we have partnered with Civic Giving Alliance, TeeScore.org, and Fairway Clubs Group as our tournament partners. In addition to our in-person event on August 23, golfers can also play at 6 other local courses including Stonebrook National and Willow Glen, two nationally recognized private courses from August 1 - 23. Your sponsorship and company logo will be displayed on our tournament website from June 1 through August 31, and on the players mobile scoring app throughout the tournament.</p>
    </div>
    <div class="photo grass" role="img" aria-label="Strip of grass"></div>
  </article>

  <!-- partners -->
  <article class="panel partners-panel">
    <div class="photo" role="img" aria-label="Golfers standing on the course" style="left:0;top:0;width:360px;height:100px;background:linear-gradient(180deg,#5e6a3e 0%,#7fa142 40%,#a8d152 100%)"></div>
    <svg class="abs" style="left:0;top:40px" width="360" height="80" viewBox="0 0 360 80" aria-hidden="true">
      <path d="M0 60 C120 40 240 30 360 6 L360 80 L0 80 Z" fill="var(--mist)"/>
    </svg>
    <div class="abs partners-copy">
      <h2>Our Partners:</h2>
      <ul>
        <li><svg width="9" height="9" viewBox="0 0 10 10" aria-hidden="true"><circle cx="5" cy="5" r="5" fill="var(--navy)"/><path d="M2.6 5.2l1.6 1.6 3.2-3.4" fill="none" stroke="#fff" stroke-width="1.3"/></svg>Civic Giving Alliance</li>
        <li><svg width="9" height="9" viewBox="0 0 10 10" aria-hidden="true"><circle cx="5" cy="5" r="5" fill="var(--navy)"/><path d="M2.6 5.2l1.6 1.6 3.2-3.4" fill="none" stroke="#fff" stroke-width="1.3"/></svg>TeeScore.org</li>
        <li><svg width="9" height="9" viewBox="0 0 10 10" aria-hidden="true"><circle cx="5" cy="5" r="5" fill="var(--navy)"/><path d="M2.6 5.2l1.6 1.6 3.2-3.4" fill="none" stroke="#fff" stroke-width="1.3"/></svg>Fairway Clubs Group</li>
      </ul>
      <h3>The Civic Giving Alliance:</h3>
      <p>a 501(c)(3) nonprofit organization with a Platinum rating from CharityLens. It has been serving other nonprofit organizations for over 20 years and has donated over $38 million for worthy causes, and has been a partner to BPT for 2 years.</p>
      <h3>TeeScore.org:</h3>
      <p>The sport has, for decades, brought people together, rallying individuals, communities, and businesses around efforts that focus resources on under-served communities. In short, golf is a powerful force for good. TeeScore.org helps charities, foundations, associations, social clubs, civic groups, and other nonprofits and individuals harness that power.</p>
      <h3>Fairway Clubs Group:</h3>
      <p>the largest owner and operator of more than 200 private golf and country clubs, city, and stadium clubs in markets all across the country. Bringing people together is their passion. They are a community and lifestyle for golfers, thought leaders, foodies, dynamic women, young executives, and families.</p>
      <p>Please join Bright Paths Together in sponsoring the 2021 Beacons of Promise Charity Golf Tournament. We have many different sponsorship levels available (please see the attached document). Help us provide safe &amp; sustainable neuro-inclusive co-housing communities for adults with autism or other intellectual disabilities by completing the attached Sponsorship form. In order to secure the hole signs, pin flags, banners, and other custom sponsorship items, we would ask that you return it no later than June 1.</p>
      <p class="signoff" style="margin-top:30px">Thank you for your consideration!</p>
      <p class="signoff" style="margin-top:14px">BPT Beacons of Promise Committee Chair</p>
    </div>
    <div class="photo grass" role="img" aria-label="Strip of grass"></div>
  </article>

  <!-- donate -->
  <article class="panel donate-panel">
    <svg class="abs" style="left:0;top:0" width="360" height="360" viewBox="0 0 360 360" aria-hidden="true">
      <path d="M0 0 L28 0 C4 80 0 200 22 360 L0 360 Z" fill="var(--paper)"/>
    </svg>
    <div class="photo" role="img" aria-label="Group of three golfers celebrating on a sunny course" style="left:10px;top:-60px;width:400px;height:400px;border-radius:50%;border:4px solid var(--paper);background:linear-gradient(180deg,#a9c4d4 0%,#6f8a52 30%,#4f7a35 50%,#78b640 75%,#8cc94a 100%)"></div>
    <div class="photo" role="img" aria-label="Golf club addressing a ball on a tee at sunset" style="left:96px;top:310px;width:190px;height:210px;border-radius:50%;border:4px solid var(--navy);background:radial-gradient(circle at 42% 28%,#ffd98a,#e7a646 30%,#b7832f 55%,#7c8a34 80%,#5d7a2a 100%)"></div>
    <div class="abs donate-copy">
      <h2>BRIGHT PATHS<br>TOGETHER</h2>
      <p>Providing lifelong neuro-inclusive cohousing communities for adults with autism or other intellectual disabilities</p>
      <span class="donate-btn">DONATE TODAY</span>
    </div>
    <div class="photo grass" role="img" aria-label="Strip of grass"></div>
  </article>
</section>

</body>
</html>
```